Need a book cover design for book titled: Resting Beside the River--Simple Methods for the Crossing

This book describes and presents tools to connect with and activate the Lightbody that we all carry within us. It talks about the Lighbody, brief history, lightbody levels and offers exercises to bring light into the body.
I envision a design that shows a physical body changing into light /surrounded by light; a resurrected body ascending to higher dimensions of Spirit o anything comparable .
Updates

Target Market(s)

Mature audience of spiritual seekers and those on spiritual path

Requirements
Must have
• Space on backcover for book summary at top and title and author name on spine.

```html
<!DOCTYPE html>
<html lang="en">
<head>
<meta charset="UTF-8">
<title>Resting Beside the River — Book Cover</title>
<link href="https://fonts.googleapis.com/css2?family=Cinzel:wght@400;600&display=swap" rel="stylesheet">
<style>
  :root {
    --sky-top: #8a86d6;
    --sky-mid: #4a63b8;
    --sky-deep: #1d4f86;
    --sky-floor: #0c2430;
    --glow: #f7f4ff;
    --glow-violet: #b9a6f0;
    --glow-blue: #6f8fd8;
    --silver-light: #ffffff;
    --silver-mid: #c9ccd6;
    --silver-dark: #7d8190;
    --ink-pale: #e6e8f2;
  }
  * { margin: 0; padding: 0; box-sizing: border-box; }
  html, body { width: 800px; height: 1200px; overflow: hidden; background: var(--sky-floor); }
  .cover {
    position: relative;
    width: 800px;
    height: 1200px;
    overflow: hidden;
    background:
      radial-gradient(ellipse 60% 35% at 50% 18%, rgba(210,200,250,0.75), transparent 70%),
      linear-gradient(180deg, var(--sky-top) 0%, var(--sky-mid) 35%, var(--sky-deep) 65%, var(--sky-floor) 100%);
    font-family: 'Cinzel', serif;
    text-align: center;
  }
  .lightbody-art {
    position: absolute;
    left: 100px;
    top: 110px;
    width: 600px;
    height: 820px;
  }
  .author-name {
    position: absolute;
    top: 52px;
    left: 0;
    width: 100%;
    font-size: 62px;
    line-height: 1;
    font-weight: 400;
    letter-spacing: 0.26em;
    padding-left: 0.26em;
    color: var(--ink-pale);
  }
  .title {
    position: absolute;
    top: 770px;
    left: 0;
    width: 100%;
    font-weight: 400;
    line-height: 1;
    background: linear-gradient(180deg, var(--silver-light) 0%, var(--silver-mid) 45%, var(--silver-dark) 55%, var(--silver-light) 100%);
    -webkit-background-clip: text;
    background-clip: text;
    color: transparent;
    filter: drop-shadow(0 2px 2px rgba(0,0,0,0.45));
  }
  .title-main { display: block; font-size: 132px; }
  .title-rest { display: block; font-size: 66px; margin-top: 12px; }
  .divider {
    position: absolute;
    top: 1018px;
    left: 196px;
    width: 408px;
    height: 24px;
  }
  .subtitle {
    position: absolute;
    top: 1078px;
    left: 0;
    width: 100%;
    font-size: 21px;
    line-height: 1;
    letter-spacing: 0.2em;
    padding-left: 0.2em;
    color: var(--ink-pale);
  }
</style>
</head>
<body>
<main class="cover">
  <svg class="lightbody-art" viewBox="0 0 600 820" role="img" aria-label="Illustration area: a human silhouette with arms outstretched, its body turning into starry light and wrapped in swirling white energy against a cosmic violet-blue sky">
    <defs>
      <radialGradient id="aura" cx="50%" cy="34%" r="50%">
        <stop offset="0%" stop-color="var(--glow)" stop-opacity="0.95"/>
        <stop offset="30%" stop-color="var(--glow-violet)" stop-opacity="0.6"/>
        <stop offset="100%" stop-color="var(--glow-violet)" stop-opacity="0"/>
      </radialGradient>
      <radialGradient id="column" cx="50%" cy="30%" r="60%">
        <stop offset="0%" stop-color="var(--glow)" stop-opacity="0.8"/>
        <stop offset="45%" stop-color="var(--glow-blue)" stop-opacity="0.4"/>
        <stop offset="100%" stop-color="var(--glow-blue)" stop-opacity="0"/>
      </radialGradient>
    </defs>
    <ellipse cx="300" cy="290" rx="300" ry="280" fill="url(#aura)"/>
    <ellipse cx="300" cy="460" rx="150" ry="380" fill="url(#column)"/>
  </svg>

  <p class="author-name">AUTHOR NAME</p>

  <h1 class="title">
    <span class="title-main">RESTING</span>
    <span class="title-rest">BESIDE THE RIVER</span>
  </h1>

  <svg class="divider" viewBox="0 0 408 24" aria-hidden="true">
    <line x1="0" y1="12" x2="408" y2="12" stroke="var(--ink-pale)" stroke-width="2"/>
    <ellipse cx="204" cy="12" rx="10" ry="5" fill="var(--ink-pale)"/>
  </svg>

  <p class="subtitle">SIMPLE METHODS FOR THE CROSSING</p>
</main>
</body>
</html>
```